Cloud Software Services Business Needs New Website Design

Our client is looking for a really modern design for their cloud services company. We have a logo, but apart from that, if you read the brief fully and digest the wireframes, we hope you will come up with a really amazing end product.

The design of the website should be professional and trustworthy, it is there to inspire confidence in the services and softwares, as well as emphasising the track record of RMV and relative knowledge and competencies.

Given all the cloud-related communications in the messaging on the site, we will need this in either the imagery or icons in the site so that we can connect the messaging with the service offering.

The brand, being black, gives full range for the designer to present a palette that serves the brand, not forgetting the audience are generally IT decision-makers.

Target Market(s)

Managers and Directors Responsible for IT/Cloud Infrastructure

Industry/Entity Type

IT Technology

Number of Pages Required

5+ page

Font styles to use
Sans Serif

Requirements
Must have
• Initial designs which match the brief and wireframes, focus on the homepage and the winning designer will need to supply the internal pages for the website.
Nice to have
• Clearly considered professional website designs, with consistent design work and branding. If choosing stock imagery, then from PixHarbor Basics please.
Should not have
• Not too much colour, or too consumer/youthful.

```html
<!DOCTYPE html>
<html lang="en">
<head>
<meta charset="utf-8">
<title>RMV – Cloud Services</title>
<link href="https://fonts.googleapis.com/css2?family=Inter:wght@400;500;600;700;800&display=swap" rel="stylesheet">
<style>
:root{
  --ink:#111111;
  --white:#ffffff;
  --band:#f2f2f2;
  --blue:#1e88e5;
  --blue-deep:#1565c0;
  --blue-light:#5ec8f2;
  --blue-pale:#cfeafb;
  --rose:#d83a64;
  --frame:#2b8fd3;
  --footer-head:#3b4b6b;
  --muted:#8a8f99;
  --tile:#dcdcdc;
}
*{margin:0;padding:0;box-sizing:border-box}
html,body{width:1200px;height:1200px;overflow:hidden;background:var(--white);font-family:'Inter',sans-serif;color:var(--ink)}
.page{position:absolute;left:468px;top:0;width:426px;height:1932px;transform:scale(0.6211);transform-origin:0 0;background:var(--white)}
.abs{position:absolute}
.band{position:absolute;left:0;width:426px;background:var(--band)}
.center{left:0;width:426px;text-align:center}
.btn{position:absolute;background:var(--ink);color:var(--white);font-weight:700;font-size:5.5px;display:flex;align-items:center;justify-content:center;letter-spacing:.2px;text-decoration:none}
.art{position:absolute}
.art-hero{left:128px;top:18px;width:150px;height:150px;border-radius:18px;opacity:.75;background:linear-gradient(155deg,var(--blue-light) 0%,var(--blue) 45%,var(--blue-pale) 100%)}
.art-stack{left:104px;top:310px;width:88px;height:70px;border-radius:12px;background:linear-gradient(180deg,var(--rose) 0%,#6b7fe0 28%,var(--blue) 55%,var(--blue-pale) 100%)}
.art-platform{left:243px;top:392px;width:82px;height:66px;border-radius:10px;background:linear-gradient(160deg,var(--blue) 0%,var(--blue-light) 35%,var(--blue-pale) 75%,#eef7fd 100%)}
.art-network{left:198px;top:678px;width:172px;height:116px;border-radius:12px;background:linear-gradient(135deg,var(--blue-pale) 0%,var(--blue-light) 35%,var(--blue) 60%,var(--blue-pale) 100%)}
.art-figure{left:288px;top:1030px;width:46px;height:110px;border-radius:10px;background:linear-gradient(180deg,var(--blue) 0%,var(--blue-light) 60%,var(--blue-pale) 100%)}
.art-towers{left:86px;top:60px;width:74px;height:92px;border-radius:10px;background:linear-gradient(150deg,var(--blue-deep) 0%,var(--blue) 40%,var(--blue-light) 70%,#e4f2fb 100%)}
.site-header{position:absolute;left:0;top:0;width:426px;height:38px;background:var(--ink)}
.brand{position:absolute;left:65px;top:9px;color:var(--white);font-size:16px;font-weight:500;letter-spacing:-.5px}
.nav a{position:absolute;color:var(--white);font-size:4.8px;font-weight:700;text-decoration:none}
.nav a.current{border-bottom:1px solid var(--white);padding-bottom:1px}
.hero-title{font-size:15.5px;font-weight:800;letter-spacing:.1px;position:absolute}
.sec-title{font-size:10px;font-weight:700;line-height:1.3}
.caps-title{font-size:11px;font-weight:700}
.body-text{font-size:5.8px;line-height:1.42;font-weight:500}
.promise{position:absolute;width:50px;height:50px;border:1.5px solid var(--frame);background:var(--white);top:557px}
.promise .num{position:absolute;left:18px;top:-7px;width:12px;height:12px;background:var(--blue-light);color:var(--white);font-size:5px;font-weight:700;display:flex;align-items:center;justify-content:center}
.promise p{position:absolute;left:3px;right:3px;top:19px;font-size:4.8px;font-weight:600;text-align:center;line-height:1.3}
.provider{position:absolute;top:900px;width:64px;height:70px;border:1.5px solid var(--frame);background:var(--band)}
.provider .mark{position:absolute;left:20px;top:-9px;width:24px;height:18px;background:var(--white);border:1.5px solid var(--frame)}
.provider .mark i{position:absolute;left:7px;top:4px;width:8px;height:8px;background:var(--blue)}
.provider .label{position:absolute;left:0;width:100%;top:21px;text-align:center;font-size:5px;font-weight:600}
.provider .btn{left:12px;top:45px;width:40px;height:15px;font-size:4.8px}
.blog-card{position:absolute;top:1515px;width:73px}
.blog-card .thumb{height:77px;background:var(--tile);position:relative}
.blog-card .thumb span{position:absolute;left:10px;top:6px;width:53px;height:64px;border-radius:8px;background:linear-gradient(180deg,var(--blue-light),var(--blue) 60%,var(--blue-deep))}
.blog-card h3{font-size:6.4px;font-weight:500;margin-top:10px;line-height:1.25}
.client{position:absolute;display:flex;align-items:center;gap:4px;font-size:5.4px;font-weight:700}
.client i{width:15px;height:15px;border-radius:50%;background:var(--blue)}
.foot-col{position:absolute;top:1810px}
.foot-col h4{font-size:7px;font-weight:600;color:var(--footer-head);margin-bottom:6px}
.foot-col li{list-style:none;font-size:4.2px;color:var(--muted);line-height:10px}
.badge{position:absolute;top:1870px;width:20px;height:23px;border-radius:4px;background:#dfe6ee}
.social{position:absolute;top:1866px;width:6px;height:6px;border-radius:50%}
.arrow{position:absolute;top:928px;width:0;height:0;border-top:9px solid transparent;border-bottom:9px solid transparent}
</style>
</head>
<body>
<div class="page">

  <header class="site-header">
    <div class="brand">rmv</div>
    <nav class="nav">
      <a style="left:222px;top:7px">Partners</a>
      <a style="left:259px;top:7px">Blog</a>
      <a style="left:284px;top:7px">About Us</a>
      <a style="left:322px;top:7px">Contact Us</a>
      <a class="current" style="left:228px;top:20px">Home</a>
      <a style="left:257px;top:20px">Cloud</a>
      <a style="left:286px;top:20px">Services</a>
      <a style="left:323px;top:20px">Software</a>
    </nav>
  </header>

  <section class="band" style="top:38px;height:204px">
    <div class="art art-hero" role="img" aria-label="Isometric blue cloud over servers with a robot arm"></div>
    <h1 class="center hero-title" style="top:55px">OPERATING UNDER A CLOUD?</h1>
    <h2 class="center hero-title" style="top:130px">THERE IS A SILVER LINING.</h2>
    <a class="btn" style="left:74px;top:172px;width:75px;height:18px">REDUCING COSTS</a>
    <a class="btn" style="left:175px;top:172px;width:75px;height:18px">MIGRATION</a>
    <a class="btn" style="left:277px;top:172px;width:75px;height:18px">WORK WITH US</a>
  </section>

  <section>
    <h2 class="abs center sec-title" style="top:264px">Did the promise of Cloud<br>Computing Happen For you?</h2>
    <div class="art art-stack" role="img" aria-label="Stacked blue database with a red top layer"></div>
    <p class="abs body-text" style="left:212px;top:328px;width:115px">We didn't think so! You are not alone. There are many companies just like you who believed in the promise of cloud computing but are now shackled by it.</p>
    <p class="abs body-text" style="left:103px;top:397px;width:100px">But There is a SILVER LINING which is that RMV have built a business around helping companies improve their cloud efficiencies, reduce costs and simplify their operations as a result.</p>
    <div class="art art-platform" role="img" aria-label="Blue robot hand above a glass platform"></div>
  </section>

  <section class="band" style="top:478px;height:179px">
    <h2 class="abs center sec-title" style="top:22px">It can be summarised in<br>three promises RMV makes<br>to every client or partner.</h2>
  </section>
  <div class="promise" style="left:128px"><span class="num">1</span><p>Reduce cloud costs, without moving supplier</p></div>
  <div class="promise" style="left:196px"><span class="num">2</span><p>Easily migrate from one cloud to another.</p></div>
  <div class="promise" style="left:264px"><span class="num">3</span><p>Simplify cloud management with favorite provider.</p></div>
  <p class="abs" style="left:98px;top:625px;font-size:4.8px;font-weight:500">If you already know or want to talk to us just call 01632 960 418 or</p>
  <a class="btn" style="left:273px;top:621px;width:54px;height:14px;font-weight:500">Send an email</a>

  <section>
    <h2 class="abs sec-title" style="left:68px;top:704px;font-size:9.5px;font-weight:800;line-height:1.22">YOUR CLOUD, YOUR TOOLS<br>A SUITE OF SOFTWARE TO<br>SIMPLIFY DEPLOYMENT.</h2>
    <a class="btn" style="left:68px;top:750px;width:68px;height:14px;font-size:5px">CLOUD SOFTWARE</a>
    <div class="art art-network" role="img" aria-label="Isometric network of blue cubes linked to a cloud"></div>
  </section>

  <section class="band" style="top:812px;height:197px">
    <h2 class="abs center caps-title" style="top:48px">HOW HARD IT IS TO MOVE YOUR CLOUD?</h2>
  </section>
  <span class="arrow" style="left:66px;border-right:8px solid var(--blue)"></span>
  <span class="arrow" style="left:353px;border-left:8px solid var(--blue)"></span>
  <div class="provider" style="left:95px"><span class="mark"><i></i></span><span class="label">STRATUS</span><a class="btn">VIEW MORE</a></div>
  <div class="provider" style="left:181px"><span class="mark"><i></i></span><span class="label">NIMBO</span><a class="btn">VIEW MORE</a></div>
  <div class="provider" style="left:265px"><span class="mark"><i></i></span><span class="label">CIRRIX</span><a class="btn">VIEW MORE</a></div>

  <section>
    <h2 class="abs" style="left:66px;top:1037px;font-size:7.8px;font-weight:700">KNOWLEDGEABLE INDEPENDENT ADVICE MATTERS</h2>
    <p class="abs body-text" style="left:66px;top:1056px;width:162px;font-size:5px;font-weight:600">traditionally, the balance of power lies with your host, who has no interest in moving to another platform. It may be that your cloud supplier is linked to your IT firm, developer or even staff preferences, and in some cases they will specialise n only one of these suppliers.</p>
    <p class="abs body-text" style="left:66px;top:1096px;width:162px;font-size:5px;font-weight:600">It is time to break free, RMV equips companies, resellers and consultants with the power to choose, negotiate, and move. We can do this for you.</p>
    <div class="art art-figure" role="img" aria-label="Blue figure standing on a stacked platform"></div>
  </section>

  <section class="band" style="top:1158px;height:185px">
    <h2 class="abs center caps-title" style="top:28px;left:-10px">MAKE YOUR CLOUD COSTS EVAPORATE</h2>
    <div class="art art-towers" role="img" aria-label="Blue server towers on a round base"></div>
    <p class="abs body-text" style="left:186px;top:74px;width:160px;font-size:4.9px;font-weight:600">As cloud costs continue to escalate, and as you suddenly hit new tiers of spend, you may feel helpless in the face of rising costs.</p>
    <p class="abs body-text" style="left:186px;top:100px;width:160px;font-size:4.9px;font-weight:600">However, even taking the cost of moving into account. RMV has estimated the average client will save 20% of spend on their cloud by using us to find the best solution and help you to move there.</p>
    <a class="btn" style="left:285px;top:137px;width:75px;height:17px;font-size:6px">SEE CASE STUDIES</a>
  </section>

  <section>
    <h2 class="abs center caps-title" style="top:1371px;left:-10px;font-size:11.5px">LET'S GET STARTED</h2>
    <p class="abs body-text" style="left:98px;top:1395px;width:230px;text-align:center;font-size:4.8px;font-weight:600">If you would like to speak to a friendly and helpful member of our team, ask questions, discuss option or to help with anything on your mind, please get in touch.</p>
    <a class="btn" style="left:138px;top:1426px;width:65px;height:14px;font-size:4.8px">CALL 01632 960 418</a>
    <a class="btn" style="left:232px;top:1426px;width:65px;height:14px;font-size:4.8px">SEND AN EMAIL</a>
  </section>

  <section class="band" style="top:1468px;height:168px">
    <h2 class="abs center caps-title" style="top:22px;left:-4px;font-size:11.5px">RMV BLOG</h2>
  </section>
  <article class="blog-card" style="left:44px"><div class="thumb" role="img" aria-label="Blue server stack image"><span></span></div><h3>NEWS HEADLINE OR BLOG POST</h3></article>
  <article class="blog-card" style="left:131px"><div class="thumb" role="img" aria-label="Blue server stack image"><span></span></div><h3>NEWS HEADLINE OR BLOG POST</h3></article>
  <article class="blog-card" style="left:218px"><div class="thumb" role="img" aria-label="Blue server stack image"><span></span></div><h3>NEWS HEADLINE OR BLOG POST</h3></article>
  <article class="blog-card" style="left:306px"><div class="thumb" role="img" aria-label="Blue server stack image"><span></span></div><h3>NEWS HEADLINE OR BLOG POST</h3></article>

  <section>
    <h2 class="abs center caps-title" style="top:1670px;left:-6px;font-size:11.5px">TRUSTED BY</h2>
    <div class="client" style="left:50px;top:1705px"><i></i>Company Name</div>
    <div class="client" style="left:137px;top:1705px"><i></i>Company Name</div>
    <div class="client" style="left:224px;top:1705px"><i></i>Company Name</div>
    <div class="client" style="left:311px;top:1705px"><i></i>Company Name</div>
    <div class="client" style="left:50px;top:1746px"><i></i>Company Name</div>
    <div class="client" style="left:137px;top:1746px"><i></i>Company Name</div>
    <div class="client" style="left:224px;top:1746px"><i></i>Company Name</div>
    <div class="client" style="left:311px;top:1746px"><i></i>Company Name</div>
  </section>

  <footer>
    <div class="foot-col" style="left:69px"><h4>Cloud Services</h4><ul><li>Stratus</li><li>Nimbo</li><li>Cirrix</li><li>Orbis</li><li>Kestrel</li><li>Private Cloud</li><li>Others</li></ul></div>
    <div class="foot-col" style="left:149px"><h4>Services</h4><ul><li>Cloud Cost Review</li><li>Migration Planning</li><li>Migration Execution</li><li>Security &amp; Compliance</li></ul>
      <h4 style="margin-top:9px">Software</h4><ul><li>Skyport</li><li>Driftline</li></ul></div>
    <div class="foot-col" style="left:229px"><h4>About RMV</h4><ul><li>Blog</li><li>Partners</li><li>About Us</li><li>Contact Us</li></ul></div>
    <div class="foot-col" style="left:286px"><h4>Get In Touch</h4><ul><li style="line-height:6px">Harbour House</li><li style="line-height:6px">Mill Lane</li><li style="line-height:6px">Eastbrook</li><li style="line-height:6px">EB4 2QT</li><li style="line-height:6px">England</li></ul></div>
    <span class="badge" style="left:231px"></span>
    <span class="badge" style="left:258px;border-radius:50%;background:#2d5a8a"></span>
    <span class="social" style="left:287px;background:var(--blue)"></span>
    <span class="social" style="left:300px;background:#c2407a"></span>
    <span class="social" style="left:313px;background:var(--blue-light)"></span>
    <span class="social" style="left:326px;background:#e53935"></span>
    <p class="abs center" style="top:1916px;font-size:3px;color:var(--muted)">Made With Care By RMV UK All Rights Reserved</p>
  </footer>

</div>
</body>
</html>
```